Graphics for Blog Post Series

We are looking for 3 infographic style designs (see attached examples) to be used in a blog post series about CDL training. This blog post series includes 3 separate posts (links provided below) and the graphics should have a consistent look and feel across all 3 posts.

The point of each graphic is to have a visual representation of content discussed in each post and tell the story of that post. It should be something that will allow people to get an idea of what the post is about by looking at a visual.

The 3 mini graphics can be used independently with each post or all as one larger image that flows together (as shown in the attached example)

The size of each individual image should be 802 X 372. The size of all images put together (stacked on top of each other) should be 802 X 1117

Blog Post #1: http://bluefernlearning.example/blog/top-10-reasons-to-choose-company-sponsored-cdl-training/

Ideas for graphic: some type of graphic to represent a Top 10 List with a couple numbers and examples from the post. Text can be used to make the purpose of the image clear (as shown in example)

Blog Post #2: http://bluefernlearning.example/blog/pay-for-cdl-training/

Ideas for graphic: graphic showing money being held up (possibly by a person's hand) and words "How to pay for CDL training"

Blog Post #3: http://bluefernlearning.example/blog/cdl-job-opportunity/

Ideas for graphic: show a truck (similar to one in pitfall example) with a flat tire and indicate visually that a CDL with no job isn't going anywhere.

Again, we want these graphics to be very similar to the examples attached as they will be used in the same manner.

Industry/Entity Type

Graphic Design

```html
<!DOCTYPE html>
<html lang="en">
<head>
<meta charset="utf-8">
<title>CDL Training Blog Series Graphics</title>
<link rel="stylesheet" href="https://fonts.googleapis.com/css2?family=Source+Sans+3:ital,wght@0,700;1,700&display=swap">
<style>
  :root {
    --green: #56b84a;
    --green-dark: #3f9b45;
    --yellow: #f9c96c;
    --yellow-deep: #e8b35a;
    --white: #ffffff;
  }
  * { margin: 0; padding: 0; box-sizing: border-box; }
  html, body { width: 1200px; height: 837px; overflow: hidden; background: var(--white); }
  body { font-family: "Source Sans 3", "Myriad Pro", Arial, sans-serif; font-weight: 700; }
  .canvas { position: relative; width: 1200px; height: 837px; background: var(--white); }

  .panel { position: absolute; top: 0; height: 837px; overflow: hidden; }
  .panel--reasons { left: 0; width: 390px; }
  .panel--payment { left: 405px; width: 390px; }
  .panel--job { left: 812px; width: 388px; }

  .band { position: absolute; left: 0; width: 100%; }
  .band--green { background: var(--green); }
  .band--yellow { background: var(--yellow); }

  .illustration { position: absolute; }
  .illustration--graduate {
    left: 100px; top: 18px; width: 190px; height: 175px;
    background: linear-gradient(180deg, var(--green-dark) 0%, var(--yellow) 55%, var(--yellow-deep) 100%);
    border-radius: 40px 40px 10px 10px;
  }
  .illustration--money {
    left: 50px; top: 0; width: 290px; height: 420px;
    background: linear-gradient(160deg, var(--yellow) 0%, var(--yellow-deep) 45%, #f4f4ee 100%);
    border-radius: 0 0 30px 30px;
  }
  .illustration--truck {
    left: 0; top: 20px; width: 388px; height: 410px;
    background: linear-gradient(180deg, var(--yellow) 0%, #eef3ea 50%, var(--yellow-deep) 100%);
  }

  .sign {
    position: absolute; left: 55px; top: 182px; width: 265px; height: 330px;
    background: var(--white); border: 8px solid var(--green); border-radius: 12px;
    color: var(--green-dark); text-align: center;
    display: flex; flex-direction: column; justify-content: center;
  }
  .sign__line { font-size: 37px; line-height: 49px; }
  .sign__sub { font-size: 21px; line-height: 36px; letter-spacing: -0.8px; }

  .reasons-list {
    position: absolute; left: 30px; top: 529px; right: 20px;
    list-style: none; color: var(--green-dark);
    font-style: italic; font-size: 16.5px; line-height: 22.3px;
  }
  .reasons-list li { display: flex; }
  .reasons-list .num { width: 24px; flex: none; }

  .headline { position: absolute; left: 0; width: 100%; text-align: center; }
  .headline--payment {
    top: 468px; color: var(--green-dark); font-size: 54px; line-height: 68px;
  }
  .headline--job {
    top: 480px; color: var(--white); font-size: 47px; line-height: 63px;
  }
</style>
</head>
<body>
<div class="canvas">

  <section class="panel panel--reasons">
    <div class="band band--green" style="top:0;height:437px"></div>
    <div class="band band--yellow" style="top:437px;height:400px"></div>
    <div class="illustration illustration--graduate" role="img" aria-label="Graduate in a mortarboard cap holding up a sign"></div>
    <div class="sign">
      <span class="sign__line">Top 10</span>
      <span class="sign__line">Reasons</span>
      <span class="sign__line">to Choose</span>
      <span class="sign__sub">(Company Sponsored)</span>
      <span class="sign__line">CDL</span>
      <span class="sign__line">Training?</span>
    </div>
    <ol class="reasons-list">
      <li><span class="num">1.</span><span>Job opportunity before training</span></li>
      <li><span class="num">2.</span><span>Don’t have enough money to pay for CDL training</span></li>
      <li><span class="num">3.</span><span>No credit checks</span></li>
      <li><span class="num">4.</span><span>No upfront tuition costs</span></li>
      <li><span class="num">5.</span><span>No loans, no interest</span></li>
      <li><span class="num">6.</span><span>Training from a reputable truck driving school</span></li>
      <li><span class="num">7.</span><span>Want to learn from instructors with proven experience</span></li>
      <li><span class="num">8.</span><span>Able to start a new career quickly</span></li>
      <li><span class="num">9.</span><span>Meet fellow drivers/teammates</span></li>
      <li><span class="num">10.</span><span>Other</span></li>
    </ol>
  </section>

  <section class="panel panel--payment">
    <div class="band band--green" style="top:0;height:440px"></div>
    <div class="band band--yellow" style="top:440px;height:397px"></div>
    <div class="illustration illustration--money" role="img" aria-label="Hand holding up a fanned stack of banknotes"></div>
    <h2 class="headline headline--payment">How<br>to pay<br>for<br>CDL<br>training</h2>
  </section>

  <section class="panel panel--job">
    <div class="band band--yellow" style="top:0;height:440px"></div>
    <div class="band band--green" style="top:440px;height:397px"></div>
    <div class="illustration illustration--truck" role="img" aria-label="Semi truck on a winding road with a flat front tire"></div>
    <h2 class="headline headline--job">A CDL<br>without a job<br>opportunity<br>is like a truck<br>with a flat tire</h2>
  </section>

</div>
</body>
</html>
```